依頼詳細
平成26年     開業しましたが、平成27年1月より院の認知度アップ、新規患者様獲得の為
合計で2万枚程度を複数回に分けて新聞折込チラシを行います。
A4サイズでのチラシデザイン制作をお願いいたします。
現在制作中のホームページへの誘導を促したいのでURL入力のスペース確保や、『鈴風台接骨院で検索』などの記載をお願いします。
URLは12月12日現在決定していない為、仮のURLでのデザイン作成をお願いいたします。

シンプルながらも手に取った方の印象に残るような折込チラシデザインをお願いいたします。
記載項目
添付資料内のロゴ・HPサンプル等をご参照いただき、院名/住所/連絡先/受付時間/地図等の記載をお願いいたします。
サイズ
A4
ページ数
片面
希望イメージ
シンプル 複雑
単色 カラフル
暗い 明るい
日常 高級
遊び心 厳粛
未来的 伝統的
女性的 男性的
希望する色
納品ファイル
• 高解像度JPG (.jpg)
• イラストレーター形式 (.ai)
補足説明
ホームページURLはわかり次第ご連絡いたします。

この度はご提案いただきまして誠にありがとうございます。
納品までスムーズにご対応いただき、感謝いたします。
またの機会がございましたらよろしくお願いいたします。

納品までスムーズにご対応いただき、感謝いたします。

短い期間にもかかわらずたくさんのご提案いただき驚いております。

```html
<!DOCTYPE html>
<html lang="ja">
<head>
<meta charset="utf-8">
<title>鈴風台接骨院 チラシ</title>
<link href="https://fonts.googleapis.com/css2?family=M+PLUS+Rounded+1c:wght@500;700;800&family=Noto+Sans+JP:wght@400;500;700;900&display=swap" rel="stylesheet">
<style>
:root{
  --navy:#2a3f66;
  --pink:#e85a8a;
  --text:#333;
  --green:#8cbf3f;
  --blue:#3f9ad6;
  --orange:#f0a030;
  --rose:#e8708f;
  --teal:#3fb3a8;
  --purple:#9b6ab8;
  --cream:#fbf7dc;
  --line:#d9d2a6;
}
*{box-sizing:border-box;margin:0;padding:0}
html,body{width:850px;height:1200px;overflow:hidden;background:#fff}
body{font-family:"Noto Sans JP",sans-serif;color:var(--text);position:relative}
.abs{position:absolute}

/* header */
.tagline{left:40px;top:20px;display:flex;align-items:center;gap:8px}
.tag-pain{background:var(--pink);color:#fff;font-weight:900;font-size:22px;width:54px;height:64px;display:flex;align-items:center;justify-content:center;border-radius:4px;writing-mode:vertical-rl;letter-spacing:1px;line-height:1}
.tag-lines{font-weight:700;color:var(--navy)}
.tag-lines .small{font-size:14px;color:var(--pink)}
.tag-lines .big{font-size:24px}
.clinic-title{left:40px;top:88px;font-family:"M PLUS Rounded 1c",sans-serif;font-weight:800;font-size:52px;color:var(--navy);letter-spacing:3px}
.motto-ring{left:545px;top:0px;width:270px;height:260px}
.motto{left:598px;top:82px;width:200px;font-family:"M PLUS Rounded 1c",sans-serif;font-weight:700;font-size:23px;color:#555;line-height:1.9;letter-spacing:4px;white-space:nowrap}
.motto span{display:block}
.motto span:last-child{padding-left:28px}

.ask{left:40px;top:160px;font-weight:900;font-size:19px;color:var(--pink)}
.bubble{background:#fff;border:1.5px solid #bbb;border-radius:50%;font-size:11px;line-height:1.45;display:flex;align-items:center;justify-content:center;text-align:center;padding:10px;color:#444}
.b1{left:30px;top:200px;width:120px;height:78px}
.b2{left:255px;top:170px;width:125px;height:80px}
.b3{left:150px;top:226px;width:118px;height:62px}

.figure{left:90px;top:230px;width:250px;height:540px;background:linear-gradient(180deg,#3a6aa8,#244d84);border-radius:110px 110px 40px 40px;opacity:.92}

/* symptoms */
.intro{left:345px;top:292px;font-size:13px;font-weight:700;color:var(--navy)}
.symptoms{left:355px;top:322px;width:470px;display:grid;grid-template-columns:repeat(3,140px);column-gap:22px;row-gap:16px}
.sym{width:122px;height:122px;border-radius:50%;color:#fff;font-weight:700;font-size:15px;line-height:1.45;display:flex;align-items:center;justify-content:center;text-align:center;margin:0 auto}
.s-green{background:var(--green)}.s-blue{background:var(--blue)}.s-orange{background:var(--orange)}
.s-rose{background:var(--rose)}.s-teal{background:var(--teal)}.s-purple{background:var(--purple)}
.note{left:345px;top:608px;font-size:13px;font-weight:700;color:var(--navy)}
.labels{left:345px;top:640px;display:flex;gap:8px}
.label{font-size:13px;font-weight:700;padding:4px 14px;border:1.5px solid;border-radius:3px;background:#fff}
.l1{color:var(--green)}.l2{color:var(--blue)}.l3{color:var(--orange)}.l4{color:var(--rose)}

/* info */
.info{left:0;top:780px;width:850px;height:420px;background:var(--cream);border-top:4px solid var(--green)}
.brand{left:30px;top:800px;display:flex;align-items:center;gap:10px;font-family:"M PLUS Rounded 1c",sans-serif;font-weight:800;font-size:34px;color:var(--navy)}
.brand .mark{width:22px;height:22px;border-radius:50%;background:var(--pink)}
.search{left:30px;top:852px;font-size:11px;font-weight:700;color:var(--pink)}
.photo{background:linear-gradient(135deg,#e9ddd0,#cdb9a6)}
.p1{left:30px;top:872px;width:150px;height:128px}
.p2{left:186px;top:872px;width:200px;height:128px}
.p3{left:30px;top:1006px;width:180px;height:120px}
.p4{left:216px;top:1006px;width:170px;height:120px}
.caption{left:30px;top:1134px;width:356px;background:var(--green);color:#fff;font-weight:700;font-size:15px;text-align:center;padding:8px 0}

.hours-head{left:410px;top:800px;font-size:13px;font-weight:700;color:var(--navy)}
.hours-note{left:640px;top:802px;font-size:10px;color:#666}
.hours{left:410px;top:822px;width:410px;border-collapse:collapse;font-size:13px;background:#fff}
.hours th,.hours td{border:1px solid var(--line);padding:4px 0;text-align:center}
.hours th{font-weight:700;color:var(--navy);background:#f3efcf}
.hours td.time{text-align:left;padding-left:8px;font-weight:700;width:170px}
.hours .ok{color:var(--pink)}
.map{left:410px;top:915px;width:210px;height:210px;background:linear-gradient(135deg,#eef0ea,#d7ddd2);border:1px solid var(--line)}
.contact{left:632px;top:915px;width:188px}
.contact-head{background:var(--pink);color:#fff;font-weight:700;font-size:14px;text-align:center;padding:5px 0}
.phone{display:flex;align-items:center;gap:6px;font-weight:900;font-size:21px;color:var(--navy);padding:8px 0 6px}
.address{font-size:11px;line-height:1.65;color:#444}
.address b{color:var(--navy)}
</style>
</head>
<body>

<div class="abs tagline">
  <div class="tag-pain">痛み</div>
  <div class="tag-lines"><div class="small">確かな知識・技術であなたの</div><div class="big">の軽減のお手伝い</div></div>
</div>
<h1 class="abs clinic-title">鈴風台接骨院</h1>

<svg class="abs motto-ring" viewBox="0 0 260 260" aria-hidden="true">
  <g>
    <circle cx="240" cy="130" r="9" fill="#f7c6d6"/><circle cx="234.6" cy="164" r="6" fill="#c8e3a6"/>
    <circle cx="219" cy="194.7" r="11" fill="#a9d4f0"/><circle cx="194.7" cy="219" r="7" fill="#fbd79e"/>
    <circle cx="164" cy="234.6" r="10" fill="#cdb5e0"/><circle cx="130" cy="240" r="6" fill="#a7ddd6"/>
    <circle cx="96" cy="234.6" r="9" fill="#f7c6d6"/><circle cx="65.3" cy="219" r="7" fill="#c8e3a6"/>
    <circle cx="41" cy="194.7" r="11" fill="#fbd79e"/><circle cx="25.4" cy="164" r="6" fill="#a9d4f0"/>
    <circle cx="20" cy="130" r="9" fill="#cdb5e0"/><circle cx="25.4" cy="96" r="7" fill="#f7c6d6"/>
    <circle cx="41" cy="65.3" r="10" fill="#a7ddd6"/><circle cx="65.3" cy="41" r="6" fill="#fbd79e"/>
    <circle cx="96" cy="25.4" r="11" fill="#c8e3a6"/><circle cx="130" cy="20" r="7" fill="#a9d4f0"/>
    <circle cx="164" cy="25.4" r="9" fill="#f7c6d6"/><circle cx="194.7" cy="41" r="6" fill="#cdb5e0"/>
    <circle cx="219" cy="65.3" r="10" fill="#fbd79e"/><circle cx="234.6" cy="96" r="7" fill="#a7ddd6"/>
  </g>
</svg>
<p class="abs motto"><span>痛みを癒し</span><span>人を助ける</span></p>

<p class="abs ask">こんな悩み、ご相談下さい!</p>
<div class="abs figure" role="img" aria-label="青い人体シルエットのイラスト（痛む部位の目印付き）"></div>
<div class="abs bubble b1">病院では異常なしと言われたけれど痛い</div>
<div class="abs bubble b2">日に日に痛みが増して、日常生活が辛くなってきた</div>
<div class="abs bubble b3">●肩が上がらない、腰が痛い</div>

<p class="abs intro">●鈴風台接骨院では、様々な身体の「痛み」「不調」に対応</p>
<div class="abs symptoms">
  <div class="sym s-green">五十肩<br>野球肩<br>むち打ち</div>
  <div class="sym s-blue">テニス肘<br>野球肘<br>手のしびれ</div>
  <div class="sym s-orange">腰痛<br>外反母趾<br>足のむくみ</div>
  <div class="sym s-rose">突き指<br>腱鞘炎</div>
  <div class="sym s-teal">ヒザ痛<br>股関節痛<br>足のしびれ</div>
  <div class="sym s-purple">ぎっくり腰<br>ヘルニアによる<br>痛み・しびれ</div>
</div>
<p class="abs note">●交通事故治療費、労災、健康保険の取り扱いが可能です</p>
<div class="abs labels">
  <span class="label l1">日常生活</span><span class="label l2">交通事故</span><span class="label l3">スポーツ</span><span class="label l4">ケガなど</span>
</div>

<section class="abs info" aria-label="院情報"></section>
<div class="abs brand"><span class="mark"></span>鈴風台接骨院</div>
<p class="abs search">ホームページ『鈴風台接骨院で検索』 www.example-clinic.jp</p>
<div class="abs photo p1" role="img" aria-label="施術風景の写真"></div>
<div class="abs photo p2" role="img" aria-label="院内の写真"></div>
<div class="abs photo p3" role="img" aria-label="手技療法の写真"></div>
<div class="abs photo p4" role="img" aria-label="物理療法機器の写真"></div>
<p class="abs caption">物理療法＆手技療法で痛みを軽減</p>

<p class="abs hours-head">受付時間案内</p>
<p class="abs hours-note">※祝日は休診となります</p>
<table class="abs hours">
  <tr><th></th><th>月</th><th>火</th><th>水</th><th>木</th><th>金</th><th>土</th><th>日</th></tr>
  <tr><td class="time">AM 8:30〜PM12:30</td><td class="ok">●</td><td class="ok">●</td><td class="ok">●</td><td class="ok">●</td><td class="ok">●</td><td class="ok">●</td><td>／</td></tr>
  <tr><td class="time">PM16:00〜PM20:00</td><td class="ok">●</td><td class="ok">●</td><td class="ok">●</td><td class="ok">●</td><td class="ok">●</td><td>／</td><td>／</td></tr>
</table>
<div class="abs map" role="img" aria-label="院周辺の地図"></div>
<div class="abs contact">
  <div class="contact-head">お電話はこちら</div>
  <div class="phone">
    <svg width="22" height="22" viewBox="0 0 24 24" aria-hidden="true"><path fill="#2a3f66" d="M6.6 10.8a15.1 15.1 0 0 0 6.6 6.6l2.2-2.2a1 1 0 0 1 1-.25 11.4 11.4 0 0 0 3.6.57 1 1 0 0 1 1 1V20a1 1 0 0 1-1 1A17 17 0 0 1 3 4a1 1 0 0 1 1-1h3.5a1 1 0 0 1 1 1c0 1.25.2 2.45.57 3.6a1 1 0 0 1-.25 1z"/></svg>
    052-555-0186
  </div>
  <p class="address"><b>【所在地】</b><br>名古屋市千種区<br>鈴風台3丁目<br>ミドリビル1F<br><b>【アクセス】</b><br>地下鉄鈴風台駅より徒歩5分<br>駐車場あり</p>
</div>

</body>
</html>
```